Visualisation and Simulation Flyer for Oil, Drone and Financial Industries

We need a flyer showcasing our visualisation and simulation technology.

For visualisation the main selling point is that the customer can easily make 'dashboards' that make huge datasets such as a year's worth of oil well pressure readings easy to use and visualise the data. Or they can load in 3D data such as an entire oilfield scanned with different sensors and look at the data VR style.

For simulation our selling point is that we can quickly make a simulation for a client, such as a drone flight simulator, and use our visualisation technology to make the resulting data very easy to use.

Our sales and marketing team need this flyer for showing initial contacts, most of which will be shown on a smartphone or tablet rather than printed out. On our website there will be a link to the flyer for people to download.

We currently sell to oil companies and the financial industries and are expanding into robotics, specifically drones and underwater robots.

We are open as to the design but need to show off a selection of the attached images and we like the colours used on our logo.

Better images and a new logo will be available in a month or two so it would be useful (not critical) if the design can easily accommodate some images being changed for new ones.

As this flyer is for multiple industries we do not want it strongly tied to any particular industry.

The flyer must use MossHarbor branding, logos are provided.

Our logos and websites www.mossharbor.example and www.quillpine.example will be outsourced and redone soon so don't use them as a guide to what we like, but they will provide some more background for you. We are using this flyer design to trial outsourcing so more work may follow.

Lots of images, videos and the logos available here: https://files.vendashare.example/s/7k2mwq9xrtpa/BQX_hYt4Lw_83Cd-nZpRkaVo?dl=0
Updates

Hi everyone, thanks for all the designs submitted so far. We are finding that we like designs with curves rather than conventional rectangular layouts with straight lines. Orange, red and yellow based colour schemes similar to our logo are also calling to us. On many designs the logo is quite isolated, it would be good to see some with the logo incorporated more strongly into the design. Many designs are focussing on the 'remote autonomous systems' but this one is really for data visualisation and simulation. We will obviously be putting our own text in but that may help you with your focus.

Target Market(s)

Oil, Drone and Financial Industries

Industry/Entity Type

Financial

Colors

Designer to choose colors to be used in the design.

Requirements
Must have
• We are open as to the design but need to show off a selection of the attached images and we like the colours used on our logo. The flyer must use MossHarbor branding, logos are provided.
Nice to have
• Better images will be available in a month or two so it would be useful (not critical) if the design can easily accommodate some images being changed for new ones.
Should not have
• As this flyer is for multiple industries we do not want it strongly tied to any particular industry.

```html
<!DOCTYPE html>
<html lang="en">
<head>
<meta charset="utf-8">
<title>MossHarbor – Visualisation and Analytics Flyer</title>
<link href="https://fonts.googleapis.com/css2?family=Lato:wght@400;700;900&display=swap" rel="stylesheet">
<style>
  :root {
    --page-bg: #eceef0;
    --brand-red: #e33b3b;
    --brand-red-deep: #c9302f;
    --brand-yellow: #f7c51c;
    --brand-orange: #f08a2b;
    --ink: #2b2b2b;
    --paper: #ffffff;
    --paper-grey: #e4e6e8;
    --screen-frame: #d5d9dd;
    --sidebar: #b9c0c7;
  }
  * { box-sizing: border-box; margin: 0; padding: 0; }
  html, body { width: 1200px; height: 848px; overflow: hidden; }
  body {
    background: var(--page-bg);
    font-family: "Lato", Arial, sans-serif;
    color: var(--ink);
  }
  .flyer {
    position: absolute;
    left: 317px; top: 24px;
    width: 566px; height: 800px;
    background: linear-gradient(180deg, var(--paper) 0%, var(--paper-grey) 55%, var(--paper) 100%);
    box-shadow: 0 6px 22px rgba(0,0,0,.18);
    overflow: hidden;
  }
  .flyer-shapes { position: absolute; inset: 0; }
  .header {
    position: absolute; left: 40px; right: 40px; top: 30px;
    text-align: center; color: var(--paper);
  }
  .header h2 {
    font-weight: 900; font-size: 25px; color: var(--brand-yellow);
    letter-spacing: .3px; margin-bottom: 8px;
  }
  .header p { font-size: 11px; line-height: 1.45; margin-bottom: 16px; }
  .callout { position: absolute; font-size: 10.5px; line-height: 1.35; font-weight: 700; }
  .callout h3 { font-size: 11px; font-weight: 900; color: var(--brand-red); }
  .callout--standard { left: 150px; top: 274px; width: 190px; }
  .callout--custom { left: 408px; top: 380px; width: 140px; }
  .callout--data { left: 40px; top: 604px; width: 230px; }
  .callout--docs { left: 310px; top: 626px; width: 220px; }
  .laptop { position: absolute; left: 24px; top: 330px; width: 370px; height: 252px; }
  .brand {
    position: absolute; left: 104px; top: 704px;
    display: flex; align-items: center; gap: 8px;
    font-size: 24px; font-weight: 400; color: var(--ink); letter-spacing: .5px;
  }
  .brand-mark { width: 16px; height: 16px; background: var(--brand-orange); }
</style>
</head>
<body>
<article class="flyer">
  <svg class="flyer-shapes" width="566" height="800" viewBox="0 0 566 800" aria-hidden="true">
    <path d="M0 0 H566 V272 Q300 256 0 248 Z" fill="var(--brand-yellow)"/>
    <path d="M0 0 H566 V264 Q300 248 0 240 Z" fill="var(--brand-red)"/>
    <path d="M0 680 L120 680 L60 740 L0 740 Z" fill="var(--brand-red)"/>
    <path d="M0 760 Q280 758 566 730 V800 H0 Z" fill="var(--paper)"/>
    <path d="M280 800 L340 768 Q450 754 566 730 V800 Z" fill="var(--brand-red)"/>
    <path d="M110 772 Q180 770 250 768 L232 786 Q170 786 110 788 Z" fill="var(--brand-red-deep)"/>
    <path d="M236 318 v12 M396 392 h10 M120 582 v20" stroke="var(--brand-orange)" stroke-width="1.2" stroke-dasharray="2 3" fill="none"/>
  </svg>

  <header class="header">
    <h2>Robust Autonomous Systems</h2>
    <p>We make autonomous and remote systems for the commercial, law enforcement and defence sectors. Our experience with the tough world of subsea robotics gives us the edge when producing robust, user-friendly systems.</p>
    <h2>Visualisation and Analytics</h2>
    <p>We accelerate development of interactive analysis and visualisation applications using our unique modular approach. From internal projects to software vendors – if you are developing a user interface for your data application we can help you.</p>
  </header>

  <section class="callout callout--standard">
    <h3>Standard Modules</h3>
    <p>We have a library of beautifully animated visualisations, from scatter charts to heat maps</p>
  </section>
  <section class="callout callout--custom">
    <h3>Custom Modules</h3>
    <p>We create to your exact specifications. Can be used alongside the standard modules.</p>
  </section>

  <svg class="laptop" viewBox="0 0 440 300" role="img" aria-label="Laptop screen showing an application dashboard with four charts">
    <defs>
      <linearGradient id="barFade" x1="0" x2="1">
        <stop offset="0" stop-color="#d7263d"/><stop offset=".35" stop-color="#f5a13a"/>
        <stop offset=".55" stop-color="#fbe7a1"/><stop offset=".75" stop-color="#8ec3e6"/>
        <stop offset="1" stop-color="#2c3f8f"/>
      </linearGradient>
      <pattern id="heatCells" width="36" height="27" patternUnits="userSpaceOnUse">
        <rect width="12" height="9" fill="#b3202a"/><rect x="12" width="12" height="9" fill="#e0675a"/><rect x="24" width="12" height="9" fill="#c73a36"/>
        <rect y="9" width="12" height="9" fill="#f0a08a"/><rect x="12" y="9" width="12" height="9" fill="#9e1b24"/><rect x="24" y="9" width="12" height="9" fill="#e8826f"/>
        <rect y="18" width="12" height="9" fill="#d24a43"/><rect x="12" y="18" width="12" height="9" fill="#f6c3b0"/><rect x="24" y="18" width="12" height="9" fill="#a92228"/>
      </pattern>
    </defs>
    <rect x="4" y="4" width="432" height="270" rx="10" fill="var(--screen-frame)"/>
    <rect x="18" y="16" width="404" height="248" fill="#f4f5f6"/>
    <path d="M0 276 H440 L428 290 H12 Z" fill="#c9ced3"/>
    <g fill="var(--sidebar)">
      <rect x="24" y="24" width="50" height="12"/><rect x="24" y="42" width="50" height="12"/>
      <rect x="24" y="60" width="50" height="12"/><rect x="24" y="78" width="50" height="12"/>
      <rect x="24" y="96" width="50" height="12"/><rect x="24" y="114" width="50" height="12"/>
      <rect x="24" y="132" width="50" height="12"/><rect x="24" y="150" width="50" height="12"/>
      <rect x="24" y="168" width="50" height="12"/><rect x="24" y="186" width="50" height="12"/>
    </g>
    <text x="250" y="32" font-family="Lato, sans-serif" font-size="13" font-weight="700" fill="#c3c8cd">Your Application</text>
    <rect x="82" y="40" width="164" height="108" fill="var(--paper)"/>
    <rect x="252" y="40" width="164" height="108" fill="var(--paper)"/>
    <rect x="82" y="154" width="164" height="104" fill="var(--paper)"/>
    <rect x="252" y="154" width="164" height="104" fill="var(--paper)"/>
    <g transform="translate(164 94)" fill="none" stroke-width="12">
      <circle r="32" stroke="#8fc6ea"/>
      <circle r="32" stroke="#2c3f8f" stroke-dasharray="40 161" transform="rotate(-90)"/>
      <circle r="32" stroke="#e33b3b" stroke-dasharray="28 173" transform="rotate(-160)"/>
      <circle r="32" stroke="#f5a13a" stroke-dasharray="30 171" transform="rotate(-215)"/>
      <circle r="32" stroke="#fbd77a" stroke-dasharray="22 179" transform="rotate(30)"/>
    </g>
    <text x="164" y="97" text-anchor="middle" font-family="Lato, sans-serif" font-size="8" fill="#555">18.0%</text>
    <g fill="url(#barFade)">
      <rect x="96" y="166" width="140" height="7"/><rect x="102" y="175" width="130" height="7"/>
      <rect x="108" y="184" width="118" height="7"/><rect x="114" y="193" width="104" height="7"/>
      <rect x="120" y="202" width="90" height="7"/><rect x="126" y="211" width="74" height="7"/>
      <rect x="132" y="220" width="58" height="7"/>
    </g>
    <path d="M170 250 L196 238 L220 242 L236 226 V250 Z" fill="#b9b4d6"/>
    <g>
      <rect x="272" y="110" width="10" height="28" fill="#c2185b"/><rect x="286" y="96" width="10" height="42" fill="#d7263d"/>
      <rect x="300" y="84" width="10" height="54" fill="#e8553e"/><rect x="314" y="74" width="10" height="64" fill="#f08a2b"/>
      <rect x="328" y="66" width="10" height="72" fill="#f5a13a"/><rect x="342" y="72" width="10" height="66" fill="#f9c85a"/>
      <rect x="356" y="82" width="10" height="56" fill="#d9e7a6"/><rect x="370" y="94" width="10" height="44" fill="#9fd3c4"/>
      <rect x="384" y="108" width="10" height="30" fill="#6fb5d8"/>
    </g>
    <rect x="282" y="164" width="126" height="81" fill="url(#heatCells)"/>
    <rect x="330" y="218" width="12" height="9" fill="#7fb3dc"/><rect x="342" y="227" width="12" height="9" fill="#2f6fb0"/>
    <rect x="318" y="236" width="12" height="9" fill="#a8cde8"/>
  </svg>

  <section class="callout callout--data">
    <h3>Data and Analytics Layer</h3>
    <p>Integrates to your data and provides a common data model to all QuillPine modules. Modules can easily be linked.</p>
  </section>
  <section class="callout callout--docs">
    <h3>Detailed Documentation</h3>
    <p>Easy to follow interactive manual for all modules classes, actions, configuration and events.</p>
  </section>

  <div class="brand"><span class="brand-mark"></span>MossHarbor</div>
</article>
</body>
</html>
```